Transport & Storage Company needs a revamp of current card

Would like to keep same colours & basic design but would like to "sharpen" up look of card.

Please remove "The Bright Haulers"

Please add 1800 419 386 on front & back of card

Please add email address on back of card - martin@brackenfreight.com.au

I would like our ABN No - 83 214 976 302 on back of card (which currently has logo only). Logo on back of card can be removed if insufficient space.

Please design another card (same as above) but with Donna Petherick - 0438 562 714, donna@brackenfreight.com.au

I do not want cards to look "too busy" so please re-arrange layout of card if necessary.

Target Market(s)

Transport & Storage

Industry/Entity Type

It Company

Contact Information for Business Card

Please refer to attached current business card

Font styles to use
Other font styles liked:
• Tahoma

Requirements
Must have
• Refer to project decsription
Nice to have
Should not have

```html
<!DOCTYPE html>
<html lang="en">
<head>
<meta charset="utf-8">
<title>Bracken Freight – Business Cards</title>
<link href="https://fonts.googleapis.com/css2?family=Arimo:wght@400;700&display=swap" rel="stylesheet">
<style>
  :root {
    --page-bg: #e9e9ec;
    --purple: #7a2f8f;
    --purple-light: #9a4bb0;
    --purple-dark: #5e1f70;
    --white: #ffffff;
    --paper: #f7f7f7;
    --grey: #8a8a8e;
    --grey-dark: #4a4a4f;
    --ink: #3c3c40;
  }
  * { box-sizing: border-box; margin: 0; padding: 0; }
  html, body {
    width: 1200px; height: 900px; overflow: hidden;
    background: var(--page-bg);
    font-family: "Arimo", Tahoma, sans-serif;
  }
  .canvas { position: relative; width: 1200px; height: 900px; }

  .card {
    position: absolute;
    width: 640px; height: 360px;
    box-shadow: 0 10px 26px rgba(0,0,0,0.22);
    overflow: hidden;
  }

  /* Back card */
  .card--back {
    left: 180px; top: 60px;
    background: radial-gradient(ellipse at 50% 20%, var(--purple-light) 0%, var(--purple) 55%, var(--purple-dark) 100%);
    color: var(--white);
    display: flex; flex-direction: column; align-items: center; justify-content: center;
    gap: 14px;
  }
  .brand-name {
    font-weight: 700;
    letter-spacing: 0.5px;
    display: flex; align-items: center; gap: 12px;
  }
  .brand-name .brand-mark { width: 18px; height: 18px; border-radius: 50%; }
  .card--back .brand-name { font-size: 46px; color: var(--white); margin-bottom: 16px; }
  .card--back .brand-mark { background: var(--white); }
  .back-line { font-size: 17px; display: flex; align-items: center; gap: 8px; }
  .back-line svg { width: 16px; height: 16px; }
  .abn { font-size: 15px; letter-spacing: 0.3px; }

  /* Front card */
  .card--front {
    left: 380px; top: 480px;
    background: linear-gradient(135deg, var(--white) 0%, var(--paper) 100%);
  }
  .card--front .brand-name {
    position: absolute; left: 36px; top: 100px;
    font-size: 40px; color: var(--purple);
  }
  .card--front .brand-mark { background: var(--purple); }
  .contact {
    position: absolute; left: 370px; top: 168px;
    color: var(--ink);
  }
  .contact-name { font-size: 21px; font-weight: 700; color: var(--purple); margin-bottom: 10px; }
  .contact-row { display: flex; align-items: center; gap: 9px; font-size: 15px; line-height: 21px; letter-spacing: 0.6px; }
  .contact-row svg { width: 13px; height: 13px; flex: none; }
  .contact-row--web { margin-top: 8px; font-size: 14px; letter-spacing: 0.2px; }

  .band-purple {
    position: absolute; left: 0; bottom: 0;
    width: 395px; height: 42px;
    background: linear-gradient(180deg, var(--purple-light), var(--purple));
  }
  .band-grey {
    position: absolute; left: 395px; bottom: 0;
    width: 245px; height: 62px;
    background: linear-gradient(180deg, var(--grey), var(--grey-dark));
  }
  .band-grey::after {
    content: ""; position: absolute; left: 0; right: 0; bottom: 0; height: 42px;
    background: var(--white); opacity: 0;
  }
</style>
</head>
<body>
<main class="canvas">

  <section class="card card--back" aria-label="Card back">
    <div class="brand-name"><span class="brand-mark"></span>Bracken Freight</div>
    <p class="back-line">
      <svg viewBox="0 0 16 16" aria-hidden="true"><rect x="1" y="3" width="14" height="10" rx="1" fill="none" stroke="#fff" stroke-width="1.5"/><path d="M1.5 3.5 L8 9 L14.5 3.5" fill="none" stroke="#fff" stroke-width="1.5"/></svg>
      martin@brackenfreight.com.au
    </p>
    <p class="abn">ABN No - 83 214 976 302</p>
  </section>

  <section class="card card--front" aria-label="Card front">
    <div class="brand-name"><span class="brand-mark"></span>Bracken Freight</div>

    <div class="contact">
      <p class="contact-name">Martin Hollis</p>
      <p class="contact-row">
        <svg viewBox="0 0 14 14" aria-hidden="true"><rect x="3.5" y="1" width="7" height="12" rx="1.2" fill="none" stroke="#4a4a4f" stroke-width="1.3"/><circle cx="7" cy="11" r="0.8" fill="#4a4a4f"/></svg>
        0451 276 830
      </p>
      <p class="contact-row">
        <svg viewBox="0 0 14 14" aria-hidden="true"><path d="M3 1.5 L5.2 1.5 L6 4.5 L4.6 5.6 Q5.8 8.2 8.4 9.4 L9.5 8 L12.5 8.8 L12.5 11 Q12.5 12.5 11 12.5 Q2 11.5 1.5 3 Q1.5 1.5 3 1.5 Z" fill="#4a4a4f"/></svg>
        1800 419 386
      </p>
      <p class="contact-row contact-row--web">
        <svg viewBox="0 0 14 14" aria-hidden="true"><circle cx="7" cy="7" r="6" fill="var(--purple)"/><path d="M1 7 H13 M7 1 Q3.5 7 7 13 M7 1 Q10.5 7 7 13" fill="none" stroke="#fff" stroke-width="0.9"/></svg>
        www.brackenfreight.com.au
      </p>
    </div>

    <div class="band-purple"></div>
    <div class="band-grey"></div>
  </section>

</main>
</body>
</html>
```